Bright Start Services (special education services) needs a Brochure Design

We need a brochure design for a new company. We are an Bright Start Services providing special education, speech, occupational and physical therapy to children birth - 3 years of age. The children we provide services for have a wide range of disabilities. Please include some stock photos if possible. Brochure text is attached.
Updates

Project Deadline Extended Reason: 1. We would like to see pictures that are multicultural (not all Caucasian).2. Some of the pictures (which were taken from our website) that were used by designers are of children that are older than 3 yrs. Please use new/different pictures of children birth-3 yrs. 3. Update the text that is in the brochure. Original line is: "The Bright Start Services (BSS) is a statewide public program for infants and toddlers with special needs". Replace with "The Bright Start Services (BSS) is a statewide public program for infants and toddlers, ages birth to 3 years, with special needs". Added Monday, February 6, 2017

Target Market(s)

Parents, Doctors, Daycare Providers

Industry/Entity Type

Education

Font styles to use
Serif
Sans Serif

Requirements
Must have
• A balance between professional looking, while child friendly and colorful
Nice to have
• A few stock pictures of children (birth-age 3)

```html
<!DOCTYPE html>
<html lang="en">
<head>
<meta charset="utf-8">
<title>Welcome to Bright Start Services</title>
<link rel="stylesheet" href="https://fonts.googleapis.com/css2?family=Arimo:wght@400;700&family=Cinzel:wght@400;500&display=swap">
<style>
:root{
  --orange:#f07022;
  --maroon:#7c4446;
  --heading-brown:#7a4243;
  --beige:#e3dcca;
  --frame:#cfc4a6;
  --ink:#231f20;
  --plum:#7b3a58;
  --phone-blue:#7fa7dd;
  --fax-purple:#a45aa6;
  --white:#ffffff;
}
*{margin:0;padding:0;box-sizing:border-box}
html,body{width:1200px;height:927px;overflow:hidden;background:var(--white)}
.brochure{position:relative;width:1200px;height:927px;background:var(--white);font-family:"Arimo",Arial,sans-serif;color:var(--ink)}
.frame{position:absolute;left:30px;top:30px;width:1140px;height:866px;border:1.5px solid var(--frame);pointer-events:none;z-index:5}
.photo{position:absolute}
.photo--family{left:30px;top:30px;width:358px;height:220px;background:linear-gradient(100deg,#b98f7c 0%,#e8cdbd 35%,#f6e7dc 65%,#fbf6f1 100%)}
.photo--nursery{left:388px;top:250px;width:812px;height:544px;background:linear-gradient(180deg,#8fcfc6 0%,#a6d8c9 22%,#c9e07f 38%,#b6d65a 70%,#d9e9a6 86%,#eef2e4 100%)}
.referrals{position:absolute;left:30px;top:250px;width:358px;height:564px;background:linear-gradient(180deg,var(--beige) 0%,#ede8da 55%,#fbfaf7 100%);padding:30px 30px 0 28px}
.referrals h2{font-weight:400;font-size:35px;color:var(--heading-brown);line-height:1;padding-bottom:6px;border-bottom:1.5px solid var(--heading-brown);width:301px}
.referrals p{font-size:12.8px;line-height:16.4px;margin-top:16.4px;width:305px}
.referrals p:first-of-type{margin-top:13px}
.hotlines{position:absolute;left:30px;top:814px;width:358px;height:82px;background:var(--maroon);color:#e7cfcf;font-size:14.4px;line-height:18.5px;padding:22px 0 0 28px}
.hotlines b{font-weight:400;color:var(--white)}
.brand{position:absolute;font-family:"Cinzel",Georgia,serif;color:var(--ink);text-transform:uppercase;letter-spacing:.5px}
.brand--top{left:440px;top:80px;width:300px;text-align:center;font-size:17px;line-height:21px}
.brand--top .brand__dot{display:block;margin:0 auto 12px;width:56px;height:56px;border-radius:50%;background:var(--orange)}
.brand--foot{left:872px;top:828px;display:flex;align-items:center;font-size:15.5px;line-height:19px}
.brand--foot .brand__dot{width:50px;height:50px;border-radius:50%;background:var(--orange);margin-right:14px}
.brand--foot .brand__name{border-left:1.5px solid var(--ink);padding-left:8px}
.title{position:absolute;left:820px;top:74px;width:350px;text-align:center;color:var(--orange);font-weight:400;font-size:41px;line-height:44px}
.contact{position:absolute;left:480px;top:376px;width:240px;text-align:center;z-index:2}
.contact__icon{display:block;margin:0 auto}
.contact__number{display:block;color:var(--white);font-size:27px;line-height:30px;text-shadow:0 2px 4px rgba(0,0,0,.45);margin:6px 0 18px}
.contact__web{display:block;color:var(--plum);font-size:20px;font-weight:700;margin-top:-2px}
.address{position:absolute;left:388px;top:852px;width:406px;height:42px;background:var(--orange);color:var(--white);font-size:14px;line-height:42px;padding-left:59px}
</style>
</head>
<body>
<div class="brochure">
  <div class="photo photo--family" role="img" aria-label="Photo of a mother cuddling her smiling baby"></div>

  <section class="referrals">
    <h2>Referrals</h2>
    <p>If you have concerns about your child’s development, you can call your county’s Bright Start Services to refer your child (please see your county’s number listed below). The Meadowbrook Center for Child Development can help you make the referral to Bright Start Services if you wish. If your child is found to be eligible for services by someone approved to perform this evaluation, you, county staff, and other team members will make a plan to help your child – and your family.</p>
    <p>Early intervention services in your plan and authorized by the county are provided at no cost to you. The county will arrange for the services to be provided and will choose the provider based on the needs of your child and family. Your child’s health insurance may be used to cover some of the costs. All other costs for BSS services are paid for by your county and New York State.</p>
    <p>Early intervention services are provided where it’s best for the child – in places such as your home, daycare, or other community settings. The BSS covers the cost of early intervention services only. The BSS does not pay for day care or other fees charged by community settings.</p>
  </section>

  <div class="hotlines">
    Referrals: Nassau County: <b>(555) 227-0166/</b><br>
    Suffolk County: <b>(555) 853-0123 / NYC: (555) 031-1000</b>
  </div>

  <div class="brand brand--top">
    <span class="brand__dot"></span>
    Meadowbrook Center for<br>Child Development
  </div>

  <h1 class="title">Welcome to<br>Bright Start<br>Services</h1>

  <div class="photo photo--nursery" role="img" aria-label="Photo of a laughing baby standing in a crib in a bright nursery"></div>

  <div class="contact">
    <svg class="contact__icon" width="46" height="46" viewBox="0 0 46 46" aria-hidden="true">
      <circle cx="23" cy="23" r="22" fill="var(--phone-blue)"/>
      <path d="M16 12c1.5-1 3-.5 3.5.8l1.7 4c.4 1-.1 2-1 2.6l-1.4.9c1 2.6 3.2 4.9 5.9 6l.9-1.4c.6-.9 1.7-1.3 2.6-.9l4 1.7c1.3.5 1.8 2 .8 3.5-1.3 2-3.4 3-5.8 2.3C19.6 29.6 15.4 25.4 13.8 19.8 13.1 17.4 14 13.4 16 12z" fill="var(--white)"/>
    </svg>
    <span class="contact__number">(555) 385-0144</span>
    <svg class="contact__icon" width="62" height="56" viewBox="0 0 62 56" aria-hidden="true">
      <rect x="2" y="18" width="12" height="36" rx="5" fill="var(--fax-purple)"/>
      <rect x="16" y="16" width="44" height="38" rx="4" fill="var(--fax-purple)"/>
      <rect x="24" y="2" width="26" height="24" fill="#f3e9f3" stroke="var(--fax-purple)" stroke-width="2"/>
      <g fill="#f3e9f3"><rect x="28" y="8" width="18" height="2"/><rect x="28" y="13" width="18" height="2"/><rect x="28" y="18" width="14" height="2"/>
      <rect x="34" y="34" width="5" height="4"/><rect x="42" y="34" width="5" height="4"/><rect x="50" y="34" width="5" height="4"/>
      <rect x="34" y="41" width="5" height="4"/><rect x="42" y="41" width="5" height="4"/><rect x="50" y="41" width="5" height="4"/>
      <rect x="20" y="34" width="10" height="11"/></g>
    </svg>
    <span class="contact__number">(555) 706-0170</span>
    <span class="contact__web">www.Meadowbrookkids.org</span>
  </div>

  <div class="address">214 Linden Avenue, Fairhaven, NY 11590</div>

  <div class="brand brand--foot">
    <span class="brand__dot"></span>
    <span class="brand__name">Meadowbrook Center for<br>Child Development</span>
  </div>

  <div class="frame"></div>
</div>
</body>
</html>
```